New Business Card Design Project

I would like to purchase a customized version of a design you have previously submitted - https://www.artmarketly.com/design/5184926<br/><br/>I need a design for a swimming pool business card. The services we provide are Maintenance, Repairs and Installations so if you include that in the card. I would also like my email bluecrestpoolsservice@mailora.com, my address 48631 Corvell Dr. Waterford CA, phone number 209-555-0173. Id like to have the two o's in Bluecrest Pools look like an actual pool.

```html
<!DOCTYPE html>
<html lang="en">
<head>
<meta charset="utf-8">
<title>Bluecrest Pools Service – Business Card</title>
<link rel="stylesheet" href="https://fonts.googleapis.com/css2?family=Open+Sans:wght@400;600&display=swap">
<style>
  :root {
    --backdrop: #3a3a37;
    --card: #121213;
    --blue: #3a8ee0;
    --white: #f2f2f2;
    --muted: #d8d8d8;
  }
  * { margin: 0; padding: 0; box-sizing: border-box; }
  html, body { width: 1200px; height: 824px; overflow: hidden; }
  body {
    background: var(--backdrop);
    font-family: "Open Sans", Arial, sans-serif;
    position: relative;
  }
  .card {
    position: absolute;
    top: 258px;
    width: 540px;
    height: 308px;
    background: var(--card);
    border-radius: 4px;
    color: var(--white);
  }
  .card--front { left: 40px; }
  .card--back { left: 620px; }

  .brand {
    position: absolute;
    display: flex;
    align-items: center;
    gap: 12px;
    color: var(--blue);
    font-weight: 400;
    letter-spacing: 0.5px;
    white-space: nowrap;
  }
  .brand__dot {
    width: 22px; height: 22px;
    border-radius: 50%;
    background: var(--blue);
    flex: none;
  }
  .card--front .brand {
    left: 50%; top: 50%;
    transform: translate(-50%, -50%);
    font-size: 30px;
  }
  .card--back .brand {
    right: 40px; top: 50px;
    font-size: 24px;
  }
  .card--back .brand__dot { width: 18px; height: 18px; }

  .services {
    position: absolute;
    right: 40px; top: 100px;
    font-size: 11.5px;
    letter-spacing: 0.6px;
    color: var(--muted);
    word-spacing: 2px;
    white-space: nowrap;
  }

  .holder {
    position: absolute;
    left: 38px; top: 176px;
    font-size: 21px;
    color: var(--white);
    white-space: nowrap;
  }
  .divider {
    position: absolute;
    left: 222px; top: 168px;
    width: 2px; height: 96px;
    background: var(--blue);
  }
  .contacts {
    position: absolute;
    left: 240px; top: 170px;
    list-style: none;
    font-size: 13px;
    line-height: 30px;
    color: var(--white);
  }
  .contacts li { display: flex; align-items: center; gap: 8px; white-space: nowrap; }
  .contacts svg { width: 13px; height: 13px; fill: var(--blue); flex: none; }
</style>
</head>
<body>
  <section class="card card--front" aria-label="Card front">
    <div class="brand"><span class="brand__dot"></span>Bluecrest Pools Service</div>
  </section>

  <section class="card card--back" aria-label="Card back">
    <div class="brand"><span class="brand__dot"></span>Bluecrest Pools Service</div>
    <p class="services">MAINTENANCE&nbsp; | &nbsp;REPAIRS&nbsp; | &nbsp;INSTALLATIONS</p>
    <p class="holder">Mateo Alvarez</p>
    <span class="divider"></span>
    <ul class="contacts">
      <li>
        <svg viewBox="0 0 24 24"><path d="M6.6 10.8a15.1 15.1 0 0 0 6.6 6.6l2.2-2.2c.3-.3.7-.4 1-.2 1.1.4 2.3.6 3.6.6.6 0 1 .4 1 1V20c0 .6-.4 1-1 1C10.6 21 3 13.4 3 4c0-.6.4-1 1-1h3.5c.6 0 1 .4 1 1 0 1.3.2 2.5.6 3.6.1.3 0 .7-.2 1z"/></svg>
        209-555-0173
      </li>
      <li>
        <svg viewBox="0 0 24 24"><path d="M2 5h20v14H2zm2 2v.5l8 5 8-5V7l-8 5z"/></svg>
        bluecrestpoolsservice@mailora.com
      </li>
      <li>
        <svg viewBox="0 0 24 24"><path d="M12 2a7 7 0 0 0-7 7c0 5.2 7 13 7 13s7-7.8 7-13a7 7 0 0 0-7-7zm0 9.5A2.5 2.5 0 1 1 12 6.5a2.5 2.5 0 0 1 0 5z"/></svg>
        48631 Corvell Dr. Larkmont CA 95517
      </li>
    </ul>
  </section>
</body>
</html>
```